Flyer for Cutting Edge Professional Learning Organization for Education Leaders

We need a two page, eye catching flyer that grabs the attention of busy school and district education leaders. It will communicate the exciting professional learning experiences that we are offering during the next school year.

We have included our two page flyer from last year. As you'll see the second page is virtually all text, so very easy to design that.

You can replicate the format of last year's flyer (LK TAMRIS 2016-17 Menu Final), making the various text changes and additions which we have included in our word document (LK TAMRIS 2017-18 Programming Flyer). Or you can go with a new format. We are open to your creativity. We are also open to either a new image that communicates the concept of leadership or one that is similar to the one we used on the first page of last year's flyer.

Target Market(s)

School and district education leaders

Industry/Entity Type

Education

Contact Information for Business Card

Logo
Lo Peterson
Executive/Program Director
lo.peterson@qmtn.example
720-555-0147
4120 Quillmont Road
Boulder, CO 80303

Font styles to use
Sans Serif

Colors
0255a3
ffffff
3176b5

Requirements
Must have
• My flyer must have the exact text which I have included on the Word document called LK TAMRIS 2017-18 Programming Flyer. We do not have time to make lots of edits and corrections to text.
• Sharp, professional and creative look.
Should not have
• No spelling or punctuation errors.

```html
<!DOCTYPE html>
<html lang="en">
<head>
<meta charset="utf-8">
<title>LK TAMRIS 2017-18 Programming</title>
<link href="https://fonts.googleapis.com/css2?family=Oswald:wght@400;500&family=Roboto+Condensed:wght@400;500;700&display=swap" rel="stylesheet">
<style>
  :root {
    --sky: #2ab4ea;
    --sky-text: #1f9bd7;
    --charcoal: #4a4a4c;
    --ink: #141414;
    --paper: #ffffff;
  }
  * { box-sizing: border-box; margin: 0; padding: 0; }
  html, body { width: 927px; height: 1200px; overflow: hidden; background: var(--paper); }
  .flyer { position: relative; width: 927px; height: 1200px; background: var(--paper); font-family: "Roboto Condensed", "Arial Narrow", sans-serif; color: var(--ink); }

  .web-tab { position: absolute; left: 34px; top: 28px; width: 600px; height: 52px; }
  .web-tab svg { position: absolute; inset: 0; }
  .web-tab p { position: relative; line-height: 52px; padding-left: 22px; color: var(--paper); font-family: "Oswald", sans-serif; font-size: 21px; font-weight: 400; letter-spacing: 0.2px; }

  .section { position: absolute; left: 54px; width: 845px; }
  .section-title { height: 56px; border-radius: 28px; background: var(--sky); color: var(--paper); text-align: center; font-family: "Oswald", sans-serif; font-weight: 400; font-size: 26px; line-height: 56px; margin-bottom: 14px; }

  .offering { padding-left: 23px; padding-right: 6px; margin-bottom: 9px; }
  .offering h3 { font-family: "Oswald", sans-serif; font-weight: 400; color: var(--sky-text); font-size: 18.5px; line-height: 22px; margin-bottom: 2px; }
  .offering p { font-size: 14.2px; font-weight: 500; line-height: 18.6px; }
  .offering.narrow p { width: 500px; }

  .quote { position: absolute; left: 596px; top: 680px; width: 284px; height: 128px; }
  .quote svg { position: absolute; inset: 0; }
  .quote p { position: relative; padding: 16px 20px 0 40px; color: var(--paper); font-size: 14.2px; font-weight: 500; line-height: 19px; }
</style>
</head>
<body>
<main class="flyer">

  <header class="web-tab">
    <svg width="600" height="52" viewBox="0 0 600 52" aria-hidden="true"><polygon points="0,0 600,0 570,52 0,52" fill="var(--charcoal)"/></svg>
    <p>Go to lktamris.org for session dates, details and facilitator bios</p>
  </header>

  <section class="section" style="top:100px">
    <h2 class="section-title">Shared Classroom Challenges</h2>
    <div class="offering">
      <h3>K-12 and Preschool Instructional Rounds:</h3>
      <p>Join other Metro Denver educator to hear diverse &nbsp;perspectives, challenge your thinking, and deepen your understanding of effective instruction and instructional leadership as you observe, discuss and reflect on key instructional challenges in K-12 and preschool classrooms. $30/session.</p>
    </div>
    <div class="offering">
      <h3>Early Literacy Systems Learning Community:</h3>
      <p>Discover how systems improvement frameworks can enhance the structures, processes and mindsets that impact early literacy results. Receive coaching and support from facilitators and learning community members as you use the frameworks to strengthen your early literacy results. &nbsp;No fee.</p>
    </div>
  </section>

  <section class="section" style="top:342px">
    <h2 class="section-title">Team Leadership</h2>
    <div class="offering">
      <h3>Feedback Fundamentals:</h3>
      <p>Through hands-on collaborative sessions, you will learn about the art and science of feedback, from cultivating a coaching mindset to practical techniques for strengthening your delivery. &nbsp;Along the way, you will build lasting relationships with a cohort of peers from across metro Denver. &nbsp;Fee is $500. &nbsp;&nbsp;This year we are offering two additional, optional sessions focusing on feedback in the context of conflict and organizational change. &nbsp;Additional fee is $200.</p>
    </div>
    <div class="offering">
      <h3>Leading Teams to the Top of Their Game:</h3>
      <p>Connect with other Metro Denver education leaders as you generate new self-insights and gain powerful tools for more effective team leadership. &nbsp;This experience uses participants' current team leadership challenges as the source for much of the cohort's discussion. Fee is $500</p>
    </div>
  </section>

  <section class="section" style="top:606px">
    <h2 class="section-title">Creative Solutions</h2>
    <div class="offering narrow">
      <h3>Design Thinking &amp; Creative Leadership:</h3>
      <p>Our hallmark learning experiences! &nbsp;Draw upon your imagination, intuition, and creative &nbsp;reasoning to think differently about problems of practice in order to make positive change in classrooms, schools, and departments. Through this unique solution-building method and with coaching support, you will put your own creative leadership into action. &nbsp;Course fee is $150. Facilitation and coaching fees vary.</p>
    </div>
  </section>

  <aside class="quote">
    <svg width="284" height="128" viewBox="0 0 284 128" aria-hidden="true"><polygon points="0,0 284,0 284,128 0,128 22,64" fill="var(--charcoal)"/></svg>
    <p>"The Design Thinking experience helped me see the great resources that surround me….my colleagues, and all our imaginations."<br>— Design Thinking participant</p>
  </aside>

  <section class="section" style="top:858px">
    <h2 class="section-title">2017-18 Pilot Programs - No fee for Pilot Participants</h2>
    <div class="offering">
      <h3>Student-Driven Learning Hub:</h3>
      <p>Design and pilot creative ways to help your staff foster student-driven learning environments. &nbsp;Build new relationships s with local, regional and national peers as you experiment with new strategies and reflect on their effectiveness.</p>
    </div>
    <div class="offering">
      <h3>Front Range Principals Club:</h3>
      <p>Join principals from across the Front Range to discuss current education issues, exchange resources, and discover helpful leadership tools. &nbsp;Business leaders will be invited to some club events. Club members will determine the club's specific activities.</p>
    </div>
    <div class="offering">
      <h3>Opportunities for Highly Experienced Leaders:</h3>
      <p>Work with other well-respected education leaders as you choose from an exciting menu of learning experiences that will help you elevate your leadership. &nbsp;Opportunities might include partnerships outside of education, stretch-to-learn experiences, and empathy experiences with students.</p>
    </div>
  </section>

</main>
</body>
</html>
```